Upgrade my Web to PHP format

I need move my web site http://kvrnode7.example to PHP format my hosting is running under Linux with MySQL , all information is on old Web site and we need move to the new Web Design , We would like to see designs that use the color of our logo.

The final design should communicate about security software , security services and hosting QLX Vanta k server.

Is very important easy installation and instructions of installation.

Target Market(s)

Bank and security company

Industry/Entity Type

Computer Security

Number of Pages Required

5+ page

Font styles to use
Sans Serif
Other font styles liked:
• arial, verdana.

Colors
3276b5
33a6d7
85cae6
85acd3
88d0c7

Requirements
Must have
• respect to our colors and all link to all pages, videos , and PDF.
Nice to have
• I would like design about security server and services , developer software security.
Should not have
• Anti Virus

```html
<!DOCTYPE html>
<html lang="en">
<head>
<meta charset="utf-8">
<title>Norvix Support — Professional IT Services &amp; Support</title>
<link rel="stylesheet" href="https://fonts.googleapis.com/css2?family=Montserrat:wght@400;500;600&family=Roboto:wght@400;500&display=swap">
<style>
:root{
  --brand:#3276b5;
  --brand-dark:#2360a0;
  --sky:#33a6d7;
  --ice:#85cae6;
  --text:#4a4a4a;
  --heading:#1e1e1e;
  --footer:#0b0d11;
  --footer-text:#c9ccd2;
  --band:#0d1a2b;
  --white:#ffffff;
}
*{margin:0;padding:0;box-sizing:border-box}
html,body{width:1200px;height:2446px;overflow:hidden}
body{position:relative;background:var(--white);font-family:"Roboto",Arial,sans-serif;color:var(--text)}
.abs{position:absolute}
h1,h2,h3,h4{font-family:"Montserrat",Arial,sans-serif;font-weight:500}

/* header */
.site-header{left:0;top:0;width:1200px;height:183px;background:linear-gradient(#ffffff,#e9eaec)}
.brand{left:111px;top:40px;display:flex;align-items:center;gap:14px}
.brand-mark{width:54px;height:54px;border-radius:50%;background:var(--brand)}
.brand-name{font-family:"Montserrat",sans-serif;font-weight:500;font-size:30px;color:var(--brand);letter-spacing:.5px}
.tagline{right:111px;top:66px;font-family:"Montserrat",sans-serif;font-weight:500;font-size:22px;color:#222;letter-spacing:.3px}
.main-nav .tab{position:absolute;top:127px;height:56px;border:1px solid #d2d3d6;border-bottom:none;background:linear-gradient(#ffffff,#eeeff1);font-family:"Roboto",sans-serif;font-size:13px;color:#333;display:flex;align-items:center;justify-content:center;text-transform:uppercase}
.main-nav .tab.active{background:var(--brand);color:#fff;border-color:var(--brand)}

/* hero */
.hero{left:0;top:183px;width:1200px;height:536px;background:linear-gradient(90deg,#7a766c 0%,#2b2f36 25%,#3a3f47 50%,#2a2d33 72%,#8b8374 100%)}
.hero-dots{left:111px;top:565px;display:flex;gap:9px}
.hero-dots span{width:13px;height:13px;border-radius:50%;background:#8d8f93}
.hero-dots span.on{background:var(--sky)}
.hero-caption{left:0;top:603px;width:1200px;height:116px;background:rgba(20,22,26,.55)}
.hero-caption h2{position:absolute;left:111px;top:28px;color:#fff;font-size:22px;font-weight:500}
.hero-caption p{position:absolute;left:111px;top:60px;width:930px;color:#f1f1f1;font-size:13px;line-height:22px}

/* principles */
.section-title{width:1200px;left:0;text-align:center;color:var(--heading);font-size:21px;letter-spacing:.5px}
.intro{left:120px;width:960px;text-align:center;font-size:12px;line-height:26px;color:#555}
.server-art{left:187px;top:905px;width:213px;height:277px;background:linear-gradient(#2a2d33,#111214 80%,#e5e5e5);border-radius:6px}
.detail{left:458px;width:640px;font-size:12px;line-height:26px;color:#555}
.sub-title{font-family:"Montserrat",sans-serif;font-weight:500;font-size:14px;color:var(--brand);letter-spacing:.3px}
.tech-list{left:458px;top:1000px;list-style:none;font-size:12px;color:#555}
.tech-list li{height:31px;display:flex;align-items:center;gap:6px}

/* features band */
.features{left:0;top:1219px;width:1200px;height:383px;background:linear-gradient(90deg,#0a121c,#16293d 50%,#0a121c)}
.feature{position:absolute;top:88px;width:300px;text-align:center;color:#fff}
.feature .ring{width:130px;height:130px;margin:0 auto;border:2px solid var(--sky);border-radius:50%;display:flex;align-items:center;justify-content:center}
.feature h3{margin-top:22px;font-size:16px;letter-spacing:.5px}
.feature p{margin-top:14px;font-size:12px;line-height:20px;color:#e8ecf1}

/* cloud */
.cloud-art{left:220px;top:1777px;width:236px;height:228px;background:radial-gradient(ellipse at center,#bfe3f6 0%,#eef6fb 45%,#ffffff 75%)}
.cloud-copy{left:527px;top:1770px;width:580px;font-size:12px;line-height:31px;color:#555}
.read-more{font-family:"Montserrat",sans-serif;font-size:12px;color:var(--brand);letter-spacing:.4px}

/* contact band */
.contact-band{left:0;top:2049px;width:1200px;height:111px;background:var(--brand);color:#fff;text-align:center}
.contact-band h2{margin-top:22px;font-size:32px;font-weight:400;letter-spacing:.5px}
.contact-band p{margin-top:4px;font-size:12px}

/* footer */
.site-footer{left:0;top:2160px;width:1200px;height:286px;background:var(--footer);color:var(--footer-text)}
.foot-brand{position:absolute;left:118px;top:60px;display:flex;align-items:center;gap:8px}
.foot-brand .brand-mark{width:30px;height:30px}
.foot-brand .brand-name{font-size:18px}
.social{position:absolute;left:112px;top:108px;display:flex;gap:6px}
.social span{width:27px;height:27px;border-radius:50%;background:var(--brand)}
.foot-col{position:absolute;top:34px}
.foot-col h4{color:#fff;font-size:16px;letter-spacing:.4px;margin-bottom:14px;height:20px}
.foot-col ul{list-style:none;font-size:11px}
.foot-col li{height:26px}
.newsletter p{font-size:11px;line-height:21px;width:260px}
.newsletter .field{margin-top:10px;width:263px;height:38px;background:#fff;border-radius:3px;color:#999;font-size:11px;padding:12px 14px}
.newsletter .btn{margin-top:8px;width:118px;height:34px;background:var(--sky);color:#fff;font-size:11px;display:flex;align-items:center;justify-content:center;border-radius:2px}
.copyright{position:absolute;left:0;top:245px;width:1200px;text-align:center;font-size:10px;color:#8a8e96}
.copyright b{font-weight:400;color:var(--sky)}
</style>
</head>
<body>

<header class="abs site-header">
  <div class="abs brand"><span class="brand-mark"></span><span class="brand-name">NORVIX SUPPORT</span></div>
  <div class="abs tagline">THE IDEAL PROFESSIONAL IT SERVICES &amp; SUPPORT.</div>
  <nav class="main-nav">
    <div class="tab active" style="left:111px;width:101px">Home</div>
    <div class="tab" style="left:225px;width:130px">About us</div>
    <div class="tab" style="left:368px;width:131px">Products</div>
    <div class="tab" style="left:512px;width:117px">Services</div>
    <div class="tab" style="left:642px;width:157px">Cloud services</div>
    <div class="tab" style="left:812px;width:117px">Contact</div>
    <div class="tab" style="left:942px;width:145px">Support ticket</div>
  </nav>
</header>

<section class="abs hero" role="img" aria-label="Photo of a businessman touching a cloud icon surrounded by device and service icons"></section>
<div class="abs hero-dots"><span></span><span class="on"></span><span></span><span></span></div>
<div class="abs hero-caption">
  <h2>ALL ABOUT IT.</h2>
  <p>Our certified IT technicians and computer engineers excel with design, deployment, and maintaining communications systems. From implementing new data management systems to upgrading security standards, we can handle all your IT needs.</p>
</div>

<h2 class="abs section-title" style="top:770px">EFFECTIVE OPERATING PRINCIPLES</h2>
<p class="abs intro" style="top:814px">We are a company with extensive experience in the area of information technology for environments QLX Vanta k (QS/400), and we are part of the ISV Business Partners. Our strength lies in the extensive knowledge and experience in the area of computer security and support in providing the best solutions, which cover the requirements of confidentiality and availability of data on that platform.</p>
<div class="abs server-art" role="img" aria-label="Illustration of a stacked server rack with a padlock"></div>
<p class="abs detail" style="top:905px">As a result of this experience, we developed the product IP Security to ensure that monitoring and access control to the QLX Vanta k.</p>
<div class="abs sub-title" style="left:458px;top:968px">WE MASTER THE FOLLOWING TECHNOLOGIES:</div>
<ul class="abs tech-list">
  <li><svg width="11" height="11" viewBox="0 0 11 11"><circle cx="5.5" cy="5.5" r="5.5" fill="#33a6d7"/><path d="M3 5.6l1.7 1.7L8 4" stroke="#fff" stroke-width="1.4" fill="none"/></svg>RPG</li>
  <li><svg width="11" height="11" viewBox="0 0 11 11"><circle cx="5.5" cy="5.5" r="5.5" fill="#33a6d7"/><path d="M3 5.6l1.7 1.7L8 4" stroke="#fff" stroke-width="1.4" fill="none"/></svg>RPGLE</li>
  <li><svg width="11" height="11" viewBox="0 0 11 11"><circle cx="5.5" cy="5.5" r="5.5" fill="#33a6d7"/><path d="M3 5.6l1.7 1.7L8 4" stroke="#fff" stroke-width="1.4" fill="none"/></svg>Ks NetFrame 2010</li>
  <li><svg width="11" height="11" viewBox="0 0 11 11"><circle cx="5.5" cy="5.5" r="5.5" fill="#33a6d7"/><path d="M3 5.6l1.7 1.7L8 4" stroke="#fff" stroke-width="1.4" fill="none"/></svg>SrvPage.NET</li>
  <li><svg width="11" height="11" viewBox="0 0 11 11"><circle cx="5.5" cy="5.5" r="5.5" fill="#33a6d7"/><path d="M3 5.6l1.7 1.7L8 4" stroke="#fff" stroke-width="1.4" fill="none"/></svg>QDB-2</li>
</ul>

<section class="abs features">
  <div class="features-bg" role="img" aria-label="Dark photo of a server room corridor" style="position:absolute;inset:0"></div>
  <div class="feature" style="left:114px">
    <div class="ring"><svg width="36" height="36" viewBox="0 0 36 36"><circle cx="18" cy="18" r="16" fill="#33a6d7"/><path d="M8 14c4-1 6 2 9 1s3 5 1 7-1 6-4 6c-1-3-4-4-3-7s-3-4-3-7zM22 7c2 2 5 2 6 6-2 1-5-1-6-3z" fill="#0d1a2b"/></svg></div>
    <h3>INTEGRATED SERVICES</h3>
    <p>Ut wisi enim ad minim veniam, quis nostrud exerci tation ullamcorper suscipit lobortis nisl ut aliquip ex ea co mmodo consequat.</p>
  </div>
  <div class="feature" style="left:450px">
    <div class="ring"><svg width="40" height="40" viewBox="0 0 40 40" fill="none" stroke="#33a6d7" stroke-width="4"><circle cx="15" cy="22" r="7" stroke-dasharray="4 2.5"/><circle cx="15" cy="22" r="2.5" stroke-width="2"/><circle cx="29" cy="11" r="5" stroke-dasharray="3 2"/><circle cx="29" cy="30" r="4" stroke-dasharray="3 2"/></svg></div>
    <h3>CUSTOMER SERVICE</h3>
    <p>Lorem ipsum dolor sit amet, consectetuer adipiscing elit, sed diam nonummy nibh euismod tincidunt ut laoreet dolore magna aliquam erat volutpat.</p>
  </div>
  <div class="feature" style="left:782px">
    <div class="ring"><svg width="38" height="38" viewBox="0 0 38 38"><circle cx="19" cy="19" r="14" fill="none" stroke="#33a6d7" stroke-width="7" stroke-dasharray="11 11" transform="rotate(-22 19 19)"/><circle cx="19" cy="19" r="17" fill="none" stroke="#33a6d7" stroke-width="1.5"/><circle cx="19" cy="19" r="9" fill="none" stroke="#33a6d7" stroke-width="1.5"/></svg></div>
    <h3>SUPPORT</h3>
    <p>Mirum est notare quam littera gothica, quam nunc puta­mus parum claram, anteposuerit litterarum formas hu­manitatis per seacula quarta.</p>
  </div>
</section>

<h2 class="abs section-title" style="top:1649px">CLOUD SERVICES</h2>
<p class="abs intro" style="top:1690px">We offer rental services for virtual servers QS/400 user or equipment, also hosting server placement and Wendex, Linux, Unix servers.<br>We specialize in providing secure high-speed connections to an QLX Vanta k (QS/400) via Internet.</p>
<div class="abs cloud-art" role="img" aria-label="Illustration of a cloud connected to computers, phone, camera, speaker and game controller"></div>
<div class="abs cloud-copy">
  <div class="sub-title" style="line-height:24px">TYPES OF SERVICES.</div>
  <p>Individual developer, and corporate accounts for small business, the developer, platform io instructors learn to program in the Vanta k (QS/400), this service allows you to work on modern computers, also application development companies have separate test environments their own systems. We have cases where companies cease completely its applications in our teams and the entire operation is handled as outsourcing.</p>
  <p>Our servers currently have installed OS 6.1 and meet the latest PTF's level available for your level.</p>
  <div class="read-more" style="margin-top:6px">READ MORE</div>
</div>

<section class="abs contact-band">
  <h2>CONTACT US &nbsp;<svg width="14" height="22" viewBox="0 0 14 22"><path d="M3 3l8 8-8 8" stroke="#fff" stroke-width="3" fill="none"/></svg></h2>
  <p>Lorem ipsum dolor sit amet, consectetuer adipiscing elit, sed diam nonummy nibh</p>
</section>

<footer class="abs site-footer">
  <div class="foot-brand"><span class="brand-mark"></span><span class="brand-name">NORVIX SUPPORT</span></div>
  <div class="social"><span></span><span></span><span></span><span></span><span></span></div>
  <div class="foot-col" style="left:365px">
    <h4>QUICK LINKS</h4>
    <ul><li>Sitemap</li><li>Newsletter Signup</li><li>Terms &amp; Conditions</li><li>Privacy Policy</li><li>Contact Us</li></ul>
  </div>
  <div class="foot-col" style="left:566px">
    <h4>ABOUT</h4>
    <ul><li>Products</li><li>Services</li><li>Cloud Services</li><li>Contact</li><li>Support Ticket</li></ul>
  </div>
  <div class="foot-col" style="left:696px">
    <h4></h4>
    <ul><li>News</li><li>Blog</li><li>Send Mail</li></ul>
  </div>
  <div class="foot-col newsletter" style="left:823px">
    <h4>NEWSLETTER SIGNUP</h4>
    <p>Enter your email address to receive our latest newsletters containing our latest News.</p>
    <div class="field">Email Address</div>
    <div class="btn">SUBSCRIBE</div>
  </div>
  <div class="copyright">Copyright © 2015 Norvix Support. 4120 Harbor Lane Suite 210 PORTVALE, ST , 00481 Phone: <b>+1 (555) 0142318</b></div>
</footer>

</body>
</html>
```